Brindle Oat Slabs - Single product design

Brindle Oat Slabs is a new protein bar company, going after the bodybuilder and powerlifter market. A high calorie, high protein, low sugar bar made of the highest quality ingredients.
We need a single product landing page that offers information, styling, and the ability to add the product to the cart at the end of it. Looking to expand soon into more flavors, it needs to be adaptable to accommodate new product offerings. A bold, yet sleek/modern design is needed to give off the image of strength, and power. Stick with the same color schemes and overall look of the product packaging (black, red, carbon fiber type background textures).
Quality | Transparency | Results * Needs to be present at the top of the page, with the ability to hover over each word to pup up a menu that shows the text listed in my word document provided. Pictures of the bar, as well as the model should be incorporated in the design. Not all images have to be used. An option to buy either a single bar, or a box is a must. With the quantity of each able to be selected.
A second page (Our Story) that describes who we are is also needed (text in word document), with a picture of the model incorporated.
Questions? Let me know! Fast answers and can get you anything you need. Thanks for everything!
Font styles to use
Requirements
Must have
- Reviews

```html
<!DOCTYPE html>
<html lang="en">
<head>
<meta charset="utf-8">
<title>Brindle Oat Slabs</title>
<link rel="stylesheet" href="https://fonts.googleapis.com/css2?family=Orbitron:wght@500;700;800&family=Arimo:ital,wght@0,400;0,700;1,400&display=swap">
<style>
:root{
  --red:#e8000e;
  --red-deep:#c8000c;
  --black:#000;
  --ink:#0d0d0d;
  --panel:#161616;
  --line:#333;
  --white:#fff;
  --muted:#8a8a8a;
  --head:'Orbitron',sans-serif;
  --body:'Arimo',sans-serif;
}
*{margin:0;padding:0;box-sizing:border-box}
html,body{width:1200px;height:3629px;overflow:hidden;background:var(--black);color:var(--white);font-family:var(--body)}
.page{position:relative;width:1200px;height:3629px}
section,header{position:absolute;left:0;width:1200px}
.abs{position:absolute}
.btn{position:absolute;display:flex;align-items:center;justify-content:center;background:var(--red);color:var(--white);font-family:var(--head);font-weight:700;font-size:15px;letter-spacing:.5px;border-radius:3px}

/* top bar */
.topbar{top:0;height:56px;background:var(--red)}
.social{position:absolute;top:16px;left:112px;display:flex;gap:5px}
.social span{width:26px;height:26px;border:1.5px solid var(--white);border-radius:50%}
.values{position:absolute;right:112px;top:20px;font-family:var(--head);font-weight:700;font-size:14px;letter-spacing:.6px}

/* nav */
.nav{top:56px;height:133px;background:var(--black)}
.brand{position:absolute;left:112px;top:36px;display:flex;align-items:center;gap:12px;font-family:var(--head);font-weight:700;font-size:30px;letter-spacing:4px}
.brand i{width:16px;height:16px;background:var(--red);display:block}
.menu{position:absolute;top:56px;display:flex;font-family:var(--head);font-weight:700;font-size:15px}
.menu a{position:absolute;white-space:nowrap;color:var(--white);text-decoration:none}
.menu a.active{color:var(--red)}
.cart{position:absolute;left:1028px;top:34px;width:60px;height:60px;border:2px solid var(--red);border-radius:50%}
.cart b{position:absolute;top:4px;left:0;width:100%;text-align:center;color:var(--red);font-weight:400;font-size:14px}

/* hero */
.hero{top:189px;height:718px;background:linear-gradient(90deg,#3a3a3a,#5a5a5a 55%,#4a4a4a)}
.hero h1{position:absolute;left:112px;top:205px;font-family:var(--head);font-weight:700;line-height:1.15}
.hero h1 small{display:block;font-size:31px}
.hero h1 span{display:block;font-size:45px}
.hero p{position:absolute;left:112px;top:315px;width:440px;font-size:18px;line-height:29px}

/* welcome */
.welcome{top:907px;height:639px;background:var(--black)}
.welcome .kicker{position:absolute;left:112px;top:122px;font-family:var(--head);font-weight:700;font-size:26px}
.welcome h2{position:absolute;left:112px;top:160px;font-family:var(--head);font-weight:700;font-size:34px;color:var(--red)}
.welcome p{position:absolute;left:112px;top:220px;width:496px;font-size:14px;line-height:25.7px;color:var(--muted);text-align:justify}
.welcome .photo{position:absolute;left:660px;top:40px;width:390px;height:599px;background:radial-gradient(ellipse at 50% 45%,#2a2a2a,#000 70%)}

/* products */
.products{top:1546px;height:608px;background:linear-gradient(180deg,#1a1a1a,#0f0f0f)}
.sec-title{position:absolute;left:0;width:100%;text-align:center;font-family:var(--head);font-weight:700;font-size:35px;color:var(--red)}
.rule{position:absolute;left:579px;width:42px;height:2px;background:var(--white)}
.card{position:absolute;top:155px;width:314px;height:355px;border:3px solid #2c2c2c;background:#111;text-align:center}
.card .shot{position:absolute;left:50px;top:25px;width:210px;height:200px;background:linear-gradient(160deg,#2b2b2b,#0b0b0b)}
.card h3{position:absolute;top:275px;width:100%;font-family:var(--head);font-weight:700;font-size:20px}
.card .price{position:absolute;top:305px;width:100%;font-family:var(--head);font-weight:700;font-size:19px;color:var(--red)}
.card.feature{background:var(--red-deep);border-color:var(--white)}
.card.feature h3{top:82px;font-size:18px;line-height:26px;padding:0 30px}
.card.feature p{position:absolute;top:147px;left:20px;right:20px;font-size:14px;line-height:26px}
.card.feature .outline{position:absolute;left:86px;top:236px;width:138px;height:47px;border:2px solid var(--white);border-radius:3px;display:flex;align-items:center;justify-content:center;font-family:var(--head);font-weight:700;font-size:14px}

/* testimonial */
.testimonial{top:2154px;height:637px;background:linear-gradient(90deg,#1c1c1c,#3b3b3b 40%,#222)}
.testimonial svg.band{position:absolute;left:0;top:0}
.quote-mark{position:absolute;left:667px;top:188px;width:74px;height:74px;border-radius:50%;background:var(--red-deep);border:2px solid #111;display:flex;align-items:center;justify-content:center;font-family:Georgia,serif;font-size:44px;font-weight:700;padding-top:18px}
.testimonial blockquote{position:absolute;left:711px;top:300px;width:425px;font-style:italic;font-size:15px;line-height:27.5px;text-align:justify}
.testimonial cite{position:absolute;left:709px;top:519px;font-style:normal;font-family:var(--head);font-weight:700;font-size:18px}
.testimonial .role{position:absolute;left:713px;top:551px;font-style:italic;font-size:14px}

/* newsletter */
.newsletter{top:2791px;height:433px;background:var(--ink)}
.newsletter p{position:absolute;left:200px;top:160px;width:800px;text-align:center;font-style:italic;font-size:15px;line-height:28px;color:var(--muted)}
.field{position:absolute;left:184px;top:239px;width:830px;height:58px;border:1px solid #777;border-radius:3px;padding:0 20px;display:flex;align-items:center;font-style:italic;font-size:15px;color:#bbb}

/* footer */
.footer{top:3224px;height:405px;background:var(--black)}
.footer .brand{left:137px;top:104px;font-size:34px}
.divider{position:absolute;top:66px;width:1px;height:124px;background:#2a2a2a}
.info{position:absolute;font-size:15px;line-height:22.5px}
.ring{position:absolute;width:42px;height:42px;border:2px solid var(--white);border-radius:50%}
.hr{position:absolute;left:112px;top:249px;width:976px;height:1px;background:#222}
.foot-menu a{position:absolute;top:290px;font-family:var(--head);font-weight:700;font-size:15px;color:var(--white);text-decoration:none;white-space:nowrap}
.copy{position:absolute;top:338px;width:100%;text-align:center;font-size:17px}
</style>
</head>
<body>
<div class="page">

  <div class="topbar">
    <div class="social"><span></span><span></span><span></span><span></span><span></span></div>
    <div class="values">QUALITY | TRANSPARENCY | RESULTS</div>
  </div>

  <header class="nav">
    <div class="brand"><i></i>BRINDLE</div>
    <nav class="menu">
      <a class="active" style="left:418px">HOME</a>
      <a style="left:521px">ABOUT US</a>
      <a style="left:663px">PRODUCT</a>
      <a style="left:798px">NEWS</a>
      <a style="left:901px">CONTACT US</a>
    </nav>
    <div class="cart"><b>0</b>
      <svg class="abs" style="left:17px;top:22px" width="24" height="20" viewBox="0 0 24 20" fill="#e8000e"><path d="M0 1h4l3 11h13l3-8H7L6 1z"/><circle cx="9" cy="17" r="2"/><circle cx="18" cy="17" r="2"/></svg>
    </div>
  </header>

  <section class="hero" role="img" aria-label="Muscular athlete curling a dumbbell in a gym">
    <h1><small>BRINDLE</small><span>OAT SLABS</span></h1>
    <p>Sed ut perspiciatis unde omnis iste natus error sit voluptatem accusantium</p>
    <a class="btn" style="left:112px;top:398px;width:148px;height:55px">READ MORE</a>
  </section>

  <section class="welcome">
    <div class="kicker">WELCOME TO</div>
    <h2>BRINDLE OAT SLABS</h2>
    <p>Sed ut perspiciatis unde omnis iste natus error sit voluptatem accusantium doloremque laudantium, totam rem aperiam, eaque ipsa quae ab illo inventore veritatis et quasi architecto beatae vitae dicta sunt explicabo. Nemo enim ipsam voluptatem quia voluptas sit aspernatur aut odit aut fugit, sed quia consequuntur magni dolores eos qui ratione voluptatem sequi nesciunt. Neque porro quisquam est, qui dolorem ipsum quia dolor sit amet, consectetur, adipisci velit, sed quia non numquam eius modi tempora incidunt ut labore et dolore magnam aliquam quaerat voluptatem. Ut enim ad minima veniam, quis nostrum exercitationem ullam laborios am, nisi ut aliquid ex ea commodi consequatur Quis autem vel eum iure vel illum qui dolorem eum fugiat quo voluptas nulla pariatur</p>
    <a class="btn" style="left:112px;top:505px;width:143px;height:52px">READ MORE</a>
    <div class="photo" role="img" aria-label="Athlete in a dark tank top standing in low light"></div>
  </section>

  <section class="products">
    <div class="sec-title" style="top:55px">OUR PRODUCT</div>
    <div class="rule" style="top:106px"></div>
    <div class="card" style="left:112px">
      <div class="shot" role="img" aria-label="Box of protein bars"></div>
      <h3>PRODUCT 01</h3>
      <div class="price">$25.99</div>
    </div>
    <div class="card feature" style="left:443px">
      <h3>SED UT PERSPICIATIS NATUS ERROR</h3>
      <p>Nemo enim ipsam voluptatem quia voluptas sit aspernatur aut odit aut fugit, sed quiacon magni dolores eos qui ratione</p>
      <div class="outline">SUBSCRIBE</div>
    </div>
    <div class="card" style="left:773px">
      <div class="shot" role="img" aria-label="Fan of wrapped protein bars"></div>
      <h3>PRODUCT 01</h3>
      <div class="price">$25.99</div>
    </div>
  </section>

  <section class="testimonial" role="img" aria-label="Athlete lifting a loaded barbell, in black and white">
    <svg class="band" width="1200" height="637" viewBox="0 0 1200 637"><polygon points="704,217 1200,217 1200,637 580,637" fill="#d4000d"/></svg>
    <div class="quote-mark">&ldquo;</div>
    <blockquote>Sed ut perspiciatis unde omnis iste natus error sit voluptatem accusantium doloremque laudantium, totam rem aperiam, eaque ipsa quae ab illo inventore veritatis et quasi architecto beatae vitae dicta sunt explicabo. Nemo enim ipsam volupt atem quia voluptas sit aspernatur aut odit aut fugit, sed quia consequuntur magni dolores eos qui ratione voluptatem sequi nesciunt neque porro quisquam est....</blockquote>
    <cite>-DALE MARROW</cite>
    <div class="role">Sed ut perspiciatis unde omnis iste natus</div>
  </section>

  <section class="newsletter">
    <div class="sec-title" style="top:82px">NEWSLETTER SIGN UP</div>
    <div class="rule" style="top:133px"></div>
    <p>Sed ut perspiciatis unde omnis iste natus error sit voluptatem accusantium doloremque laudantium, totam rem &nbsp;ab illo inventore veritatis et quasi architecto beatae vitae dicta sunt explicabo.</p>
    <div class="field">Enter Your Email :</div>
    <a class="btn" style="left:532px;top:316px;width:135px;height:47px">SUBMIT</a>
  </section>

  <footer class="footer" style="position:absolute;left:0;width:1200px">
    <div class="brand"><i></i>BRINDLE</div>
    <div class="divider" style="left:446px"></div>
    <div class="divider" style="left:774px"></div>
    <svg class="abs" style="left:489px;top:82px" width="20" height="26" viewBox="0 0 20 26" fill="none" stroke="#fff" stroke-width="1.5"><path d="M10 25S2 15 2 9a8 8 0 0 1 16 0c0 6-8 16-8 16z"/><circle cx="10" cy="9" r="3"/></svg>
    <div class="info" style="left:529px;top:72px">Address<br>P.O. Box 517 Halden Row<br>Westby MA 02980</div>
    <div class="ring" style="left:530px;top:153px"></div>
    <div class="ring" style="left:583px;top:153px"></div>
    <svg class="abs" style="left:830px;top:82px" width="22" height="22" viewBox="0 0 24 24" fill="none" stroke="#fff" stroke-width="1.5"><path d="M5 2h4l2 5-3 2a12 12 0 0 0 7 7l2-3 5 2v4a2 2 0 0 1-2 2A19 19 0 0 1 3 4a2 2 0 0 1 2-2z"/></svg>
    <div class="info" style="left:867px;top:65px">Phone:<br>000-484-2715</div>
    <svg class="abs" style="left:831px;top:143px" width="22" height="16" viewBox="0 0 22 16" fill="none" stroke="#fff" stroke-width="1.5"><rect x="1" y="1" width="20" height="14"/><path d="M1 1l10 8 10-8"/></svg>
    <div class="info" style="left:870px;top:137px">Email:<br>hello@brindleoat.com</div>
    <div class="hr"></div>
    <nav class="foot-menu">
      <a style="left:296px">HOME</a>
      <a style="left:401px">ABOUT US</a>
      <a style="left:545px">PRODUCT</a>
      <a style="left:683px">NEWS</a>
      <a style="left:789px">CONTACT US</a>
    </nav>
    <div class="copy">Brindle Oat Slabs &copy; 2021.All Rights Reserved</div>
  </footer>

</div>
</body>
</html>
```